ONLINE MATTRESS COMPANY REQUIRING BOX DESIGN FOR MATTRESS IN A BOX

WE NEED A BOX DESIGN FOR A NEW COMPANY THAT SELLS A MATTRESS IN A BOX (SIMILAR TO QUILBRAE.COM) THAT INCORPORATES ONLY 2 COLOURS (TEAL & BLACK) THE BASE COLOUR OF BOX IS WHITE. THE DESIGN HAS TO INSPIRE MILLENNIAL AND YOUNG SHOPPERS TO WANT TO PURCHASE THE PRODUCT. BOX SHOULD BE SIMPLE AND CLEAN. ONE SIDE HAS TO SHOW THE OPENING INSTRUCTIONS WHICH ARE ATTACHED IN A SAMPLE BOX.

Target Market(s)

MILLENNIALS

Industry/Entity Type

Furniture Store

Font styles to use
Serif
Sans Serif

Colors
ffffff
33b8a4

Requirements
Must have
• ONE SIDE MUST HAVE OPEN INSTRUCTIONS (SEE EXAMPLE); THE FACTORY CAN ONLY PRING ON A WHITE BOX WITH 2 COLOURS. THE WRITING AND SHAPES CAN BE TEAL AND BLACK BUT THE WHOLE BOX CANNOT BE TEAL AND BLACK, JUST THE ART WORK.
Should not have
• CAN ONLY BE 2 COLOURS; BOX COLOUR IS WHITE ; TEAL & BLACK AS OTHER INK COLOURS.

SHOULD NOT SHOW LOGO VERTICALLY (UP AND DOWN) BECAUSE IT IS HARD TO READ, SHOULD BE HORIZONTAL.

DO NOT SHOW MATTRESS OR PILLOW ON BOX IT'S ONLY TO HELP GUIDE YOU SO KNOW WHAT THE PRODUCT IS!

```html
<!DOCTYPE html>
<html lang="en">
<head>
<meta charset="utf-8">
<title>Veloa – Box Dieline</title>
<link href="https://fonts.googleapis.com/css2?family=Nunito+Sans:wght@300;400;600;700&display=swap" rel="stylesheet">
<style>
  :root {
    --teal: #00b5b2;
    --ink: #231f20;
    --paper: #ffffff;
    --crease: #d6d6d6;
    --soft-text: #8a8a8a;
    --body-text: #333333;
  }
  * { margin: 0; padding: 0; box-sizing: border-box; }
  html, body { width: 1200px; height: 778px; overflow: hidden; background: var(--paper); }
  body { font-family: "Nunito Sans", sans-serif; position: relative; }

  .dieline { position: absolute; left: 201px; top: 30px; width: 800px; height: 691px; }

  .glue-flap { position: absolute; left: 0; top: 101px; width: 32px; height: 477px; }

  .band { position: absolute; left: 32px; width: 768px; background: var(--teal); }
  .band--top { top: 0; height: 101px; }
  .band--bottom { top: 578px; height: 113px; }

  .panels { position: absolute; left: 32px; top: 101px; width: 768px; height: 477px; display: flex; }
  .panel { position: relative; width: 192px; height: 100%; border-left: 1px solid var(--crease); text-align: center; }
  .panel--instructions { background: var(--ink); border-left: none; }

  .brand-name { color: var(--teal); font-weight: 700; letter-spacing: 1px; line-height: 1; }

  .side-logo { position: absolute; top: 84px; left: 0; width: 100%; }
  .side-logo .brand-name { font-size: 30px; }

  .tagline { position: absolute; top: 256px; left: 0; width: 100%; font-size: 8px; letter-spacing: 1px; color: var(--body-text); }

  .size-note { position: absolute; top: 434px; left: 0; width: 100%; font-size: 8px; font-weight: 300; color: var(--soft-text); }

  .hang-line { position: absolute; left: 120px; top: 0; width: 1px; height: 288px; background: var(--teal); }
  .hang-dot { position: absolute; left: 118px; top: 286px; width: 4px; height: 4px; border-radius: 50%; background: var(--teal); }
  .front-logo { position: absolute; top: 306px; left: 0; width: 100%; }
  .front-logo .brand-name { font-size: 42px; }

  .steps { list-style: none; position: absolute; top: 0; left: 0; width: 100%; }
  .step { position: absolute; left: 0; width: 100%; }
  .step-icon { position: relative; width: 48px; height: 48px; margin: 0 auto; }
  .step-icon .ring { position: absolute; inset: 0; border: 2px solid var(--teal); border-radius: 50%; }
  .step-icon .art { position: absolute; inset: 10px; border-radius: 50%; background: rgba(0,181,178,0.35); }
  .step-num { position: absolute; left: 0; top: 0; width: 13px; height: 13px; border-radius: 50%; background: var(--teal); color: var(--ink); font-size: 7px; font-weight: 700; line-height: 13px; text-align: center; }
  .step-text { margin: 5px auto 0; width: 124px; color: var(--teal); font-size: 5.5px; font-weight: 700; line-height: 1.35; }

  .ink-swatches { position: absolute; left: 3px; top: 706px; display: flex; gap: 8px; }
  .ink-swatches span { width: 13px; height: 13px; border-radius: 50%; }
  .swatch--teal { background: var(--teal); }
  .swatch--black { background: #000; }
</style>
</head>
<body>
  <div class="dieline">
    <svg class="glue-flap" viewBox="0 0 32 477" aria-hidden="true">
      <polygon points="32,0 2,9 2,464 32,477" fill="none" stroke="#c8c8c8" stroke-width="1"/>
    </svg>

    <div class="band band--top" role="img" aria-label="Teal flap with a fine white dot pattern"></div>

    <div class="panels">
      <section class="panel panel--side">
        <div class="side-logo"><div class="brand-name">veloa</div></div>
        <div class="tagline">Sleep well, simply.</div>
        <div class="size-note">SIZE: 54 X 52 X 104 CM</div>
      </section>

      <section class="panel panel--front">
        <div class="hang-line"></div>
        <div class="hang-dot"></div>
        <div class="front-logo"><div class="brand-name">veloa</div></div>
      </section>

      <section class="panel panel--side">
        <div class="side-logo"><div class="brand-name">veloa</div></div>
        <div class="tagline">Sleep well, simply.</div>
        <div class="size-note">SIZE: 54 X 52 X 104 CM</div>
      </section>

      <section class="panel panel--instructions">
        <ol class="steps">
          <li class="step" style="top:30px">
            <div class="step-icon"><div class="ring"></div><div class="art" role="img" aria-label="Icon of an open box"></div><span class="step-num">1</span></div>
            <p class="step-text">Open the box from the top and lay it on its side to pull out the mattress.</p>
          </li>
          <li class="step" style="top:115px">
            <div class="step-icon"><div class="ring"></div><div class="art" role="img" aria-label="Icon of a rolled mattress unfolding"></div><span class="step-num">2</span></div>
            <p class="step-text">Now it's time to unwrap and unfold your mattress.</p>
          </li>
          <li class="step" style="top:200px">
            <div class="step-icon"><div class="ring"></div><div class="art" role="img" aria-label="Icon of a mattress with a clock"></div><span class="step-num">3</span></div>
            <p class="step-text">You can use it 2-4 hours after opening but may need 24-48 hours for optimum expansion &amp; comfort.</p>
          </li>
          <li class="step" style="top:285px">
            <div class="step-icon"><div class="ring"></div><div class="art" role="img" aria-label="Recycling icon"></div><span class="step-num">4</span></div>
            <p class="step-text">Recycle the box and do your little bit for the planet.</p>
          </li>
          <li class="step" style="top:370px">
            <div class="step-icon"><div class="ring"></div><div class="art" role="img" aria-label="Icon of a person resting on a mattress"></div><span class="step-num">5</span></div>
            <p class="step-text">Now it's time to relax and get a great night's sleep.</p>
          </li>
        </ol>
      </section>
    </div>

    <div class="band band--bottom" role="img" aria-label="Teal flap with a fine white dot pattern"></div>

    <div class="ink-swatches" aria-label="Print inks: teal and black">
      <span class="swatch--teal"></span>
      <span class="swatch--black"></span>
    </div>
  </div>
</body>
</html>
```